Etiketten für Honig
Zielgruppe
Es scheint Missverständnisse zu geben weshalb ich das Briefing wohl ändern muss.
see below for English translation
Wir sind eine kleine Imkerei, die von der Liebhaberei in den Nebenerwerb wechselt. Wir verkaufen verschiedene Sortenhonige und Honigzubereitungen (siehe Webseite) im vorwiegend ländlichen Raum des Münsterlandes.
Entsprechend unseres Standortes und unserer Kundschaft benötigen wir ein klassisch ländliches Design. Hierfür haben wir auch bereits ein Logo welches verwendet werden muss.
English
There seems to be some misunderstanding, so I guess I'll have to change the briefing.
We are a small apiary that changes from hobby to sideline. We sell different types of honey and honey preparations (e.g. honey with raspberry) in a predominantly rural area of the Münsterland (Muensterland).
According to our location and our clientele, we need a classic rural design. We already have a logo which must be used.
Aufgabenstellung
Wir möchten ein rechteckiges Etikett mit Gewährverschluss das für verschiedene Sorten adoptierbar ist. Zum Beispiel durch den Austausch der Sortenbezeichnung und eine farbliche Veränderung.
Das Design soll später auf Naturpapier oder Graspapier gedruckt werden. Das Logo muss auf Etikett und Gewährverschluss abgebildet werden.
We would like a rectangular label with a guarantee seal that is adoptable for different varieties. For example, by exchanging the variety designation and changing the color.
The design will later be printed on uncoated paper or grass paper. The logo must be shown on the label and guarantee seal.

```html
<!DOCTYPE html>
<html lang="de">
<head>
<meta charset="utf-8">
<title>Honigetiketten – Frühtracht und Waldhonig</title>
<link rel="stylesheet" href="https://fonts.googleapis.com/css2?family=Indie+Flower&family=Source+Sans+3:wght@400;600&display=swap">
<style>
  :root {
    --paper: #ffffff;
    --ink: #555555;
    --spring: #dcd731;
    --spring-text: #b9b52a;
    --forest: #35d870;
    --forest-text: #2fc463;
    --font-text: "Source Sans 3", Arial, sans-serif;
    --font-variety: "Indie Flower", cursive;
  }
  * { box-sizing: border-box; margin: 0; padding: 0; }
  html, body { width: 1200px; height: 1099px; overflow: hidden; background: var(--paper); }
  .canvas { position: relative; width: 1200px; height: 1099px; }

  .label-set { position: absolute; left: 0; width: 1200px; height: 520px; }
  .label-set--spring { top: 0; --tone: var(--spring); --tone-text: var(--spring-text); }
  .label-set--forest { top: 512px; --tone: var(--forest); --tone-text: var(--forest-text); }

  /* Guarantee seal */
  .seal-head {
    position: absolute; left: 335px; top: 45px; width: 136px; height: 136px;
    border-radius: 50%; background: var(--tone);
  }
  .seal-strip {
    position: absolute; left: 367px; top: 168px; width: 75px; height: 148px;
    background: var(--tone);
  }
  .seal-head .brand { position: absolute; left: 0; right: 0; top: 30px; }
  .seal-name {
    position: absolute; left: 17px; top: 77px; width: 102px; height: 30px;
    background: var(--paper);
    clip-path: polygon(5% 0, 95% 0, 100% 50%, 95% 100%, 5% 100%, 0 50%);
    display: flex; align-items: center; justify-content: center;
    font-family: var(--font-variety); font-size: 20px; color: var(--tone-text); letter-spacing: 1px;
  }

  /* Wrap-around label */
  .label {
    position: absolute; left: 274px; top: 314px; width: 556px; height: 185px;
    background: var(--tone);
  }
  .label .brand { position: absolute; left: 36px; top: 28px; width: 150px; }
  .variety {
    position: absolute; left: 37px; top: 117px; width: 189px; height: 39px;
    background: var(--paper);
    clip-path: polygon(6% 0, 94% 0, 100% 50%, 94% 100%, 6% 100%, 0 50%);
    display: flex; align-items: center; justify-content: center;
    font-family: var(--font-variety); font-size: 24px; color: var(--tone-text); letter-spacing: 1.5px;
  }
  .weight {
    position: absolute; left: 217px; top: 166px; width: 49px; height: 30px;
    background: var(--paper);
    clip-path: polygon(20% 0, 80% 0, 100% 50%, 80% 100%, 20% 100%, 0 50%);
    display: flex; align-items: center; justify-content: center;
    font-family: var(--font-variety); font-size: 15px; color: var(--tone-text);
  }
  .info {
    position: absolute; left: 353px; top: 31px; width: 190px; height: 135px;
    background: var(--paper);
    clip-path: polygon(3% 0, 97% 0, 100% 10%, 100% 90%, 97% 100%, 3% 100%, 0 90%, 0 10%);
    font-family: var(--font-text); color: var(--ink);
    padding: 11px 0 0 9px;
  }
  .info h2 { font-size: 11px; font-weight: 600; line-height: 1.2; }
  .info .claims { font-size: 7.2px; font-weight: 600; line-height: 1.3; margin-top: 1px; }
  .info .brand { position: absolute; left: 22px; top: 52px; width: 60px; }
  .info .address { position: absolute; left: 10px; top: 82px; font-size: 5.6px; line-height: 1.3; }
  .info .best-before { position: absolute; left: 115px; top: 82px; font-size: 5.6px; }

  /* Brand stand-in */
  .brand { display: flex; flex-direction: column; align-items: center; gap: 3px; font-family: var(--font-text); color: var(--ink); }
  .brand-dot { border-radius: 50%; background: #f3b51d; }
  .brand-name { font-weight: 600; white-space: nowrap; }
  .seal-head .brand-dot { width: 16px; height: 16px; }
  .seal-head .brand-name { font-size: 13px; }
  .label .brand-dot { width: 28px; height: 28px; }
  .label .brand-name { font-size: 21px; }
  .info .brand .brand-dot { width: 10px; height: 10px; }
  .info .brand .brand-name { font-size: 7.5px; }
  .label .info .brand { left: 22px; top: 52px; width: 60px; }
</style>
</head>
<body>
<main class="canvas">

  <section class="label-set label-set--spring" aria-label="Etikett Frühtracht">
    <div class="seal-strip" role="img" aria-label="Wabenmuster auf dem Siegelstreifen"></div>
    <div class="seal-head">
      <div class="brand"><span class="brand-dot"></span><span class="brand-name">Wabenhof</span></div>
      <div class="seal-name">Frühtracht</div>
    </div>
    <div class="label" role="img" aria-label="Etikett mit Wabenmuster">
      <div class="brand"><span class="brand-dot"></span><span class="brand-name">Wabenhof</span></div>
      <div class="variety">Frühtracht</div>
      <div class="weight">500g</div>
      <div class="info">
        <h2>Echter Honig aus dem Münsterland</h2>
        <p class="claims">Mehrwegglas, Honig aus Deutschland.<br>Trocken, dunkel und vor Wärme geschützt lagern.</p>
        <div class="brand"><span class="brand-dot"></span><span class="brand-name">Wabenhof</span></div>
        <p class="address">Honigmanufaktur Wabenhof<br>Heidkamper Weg 12<br>48999 Feldhausen<br>Tel. 02599 4710382<br>www.honigmanufaktur-wabenhof.de</p>
        <p class="best-before">Mindestens haltbar bis:</p>
      </div>
    </div>
  </section>

  <section class="label-set label-set--forest" aria-label="Etikett Waldhonig">
    <div class="seal-strip" role="img" aria-label="Wabenmuster auf dem Siegelstreifen"></div>
    <div class="seal-head">
      <div class="brand"><span class="brand-dot"></span><span class="brand-name">Wabenhof</span></div>
      <div class="seal-name">Waldhonig</div>
    </div>
    <div class="label" role="img" aria-label="Etikett mit Wabenmuster">
      <div class="brand"><span class="brand-dot"></span><span class="brand-name">Wabenhof</span></div>
      <div class="variety">Waldhonig</div>
      <div class="weight">500g</div>
      <div class="info">
        <h2>Echter Honig aus dem Münsterland</h2>
        <p class="claims">Mehrwegglas, Honig aus Deutschland.<br>Trocken, dunkel und vor Wärme geschützt lagern.</p>
        <div class="brand"><span class="brand-dot"></span><span class="brand-name">Wabenhof</span></div>
        <p class="address">Honigmanufaktur Wabenhof<br>Heidkamper Weg 12<br>48999 Feldhausen<br>Tel. 02599 4710382<br>www.honigmanufaktur-wabenhof.de</p>
        <p class="best-before">Mindestens haltbar bis:</p>
      </div>
    </div>
  </section>

</main>
</body>
</html>
```